New Website for ReBranded Company - CrewBeacon

We have a successful company and website currently but it is a little dated. We have re-branded the company from Harbor Signal Networks to CrewBeacon and have a new logo for the new name. We are looking to build a newer fresher website with the new name. I will need a concept of the home page and one inside page. You can see our current site at https://www.harborsignalnetworks.example and the new site will be https://www.crewbeacon.example .

I also really like the https://www.pathmolder.example/ website. I like ledgerleaf.example website. I like the https://skillbinder.example/ website.

See the attached document for layout and some text to use. Use the pictures I attached as opposed to pictures from the old site as much as you can.

Target Market(s)

Business

Industry/Entity Type

Software Service

Number of Pages Required

2 page

Font styles to use
Sans Serif

Requirements
Must have
• Use the colors from my logo. Professional but modern. We want people to feel like our product makes their staff feel safer at work.
Should not have
• Don't use any red or orange (no stop colors).

```html
<!DOCTYPE html>
<html lang="en">
<head>
<meta charset="utf-8">
<title>CrewBeacon — Home</title>
<link rel="stylesheet" href="https://fonts.googleapis.com/css2?family=Montserrat:wght@600;700;800&family=Lato:wght@400;700&display=swap">
<style>
:root{
  --blue:#2f8fd8;
  --blue-deep:#1f78c4;
  --green:#7ab648;
  --green-band:#8cc05a;
  --ink:#161616;
  --text:#4a4a4a;
  --muted:#6b6b6b;
  --white:#ffffff;
  --light:#f3f4f5;
}
*{box-sizing:border-box;margin:0;padding:0}
html,body{width:1200px;height:3883px;overflow:hidden}
body{font-family:"Lato",sans-serif;color:var(--text);background:var(--white);position:relative}
.abs{position:absolute}
h1,h2,h3,.heading{font-family:"Montserrat",sans-serif}
.btn{position:absolute;display:flex;align-items:center;justify-content:center;gap:10px;background:var(--blue);color:var(--white);font-family:"Montserrat",sans-serif;font-weight:600;font-size:14px;text-transform:uppercase;border-radius:3px;text-decoration:none;height:48px}
.btn.green{background:var(--green)}
.btn svg{width:14px;height:14px}
.icon-badge{position:absolute;width:56px;height:56px;border-radius:50%;background:var(--green);display:flex;align-items:center;justify-content:center}
.icon-badge svg{width:30px;height:30px}

/* header */
.site-header{position:absolute;top:0;left:0;width:1200px;height:86px;background:var(--white)}
.brand{position:absolute;display:flex;align-items:center;gap:10px}
.brand-dot{width:44px;height:44px;border-radius:50%;background:var(--blue)}
.brand-name{font-family:"Lato",sans-serif;font-weight:700;font-size:30px;color:var(--blue)}
.nav{position:absolute;left:443px;top:34px;display:flex;gap:33px;font-family:"Montserrat",sans-serif;font-weight:600;font-size:14px;color:var(--ink)}
.nav .active{color:var(--blue)}

/* hero */
.hero{position:absolute;top:86px;left:0;width:1200px;height:559px;background:linear-gradient(135deg,#4d5155 0%,#7a7f80 40%,#3a3d40 75%,#2a2c2e 100%)}
.hero-title{position:absolute;top:150px;left:0;width:1200px;text-align:center;color:var(--white);font-family:"Montserrat",sans-serif;font-weight:800;font-size:48px;line-height:57px;text-transform:uppercase}
.hero-sub{position:absolute;top:289px;left:0;width:1200px;text-align:center;color:var(--white);font-weight:700;font-size:18px;text-transform:uppercase}
.feature-card{position:absolute;top:583px;height:126px;border-radius:4px;color:var(--white);display:flex;align-items:center}
.feature-card .ic{width:90px;height:72px;border-right:1px solid rgba(255,255,255,.6);display:flex;align-items:center;justify-content:center;margin-left:8px}
.feature-card .ic svg{width:44px;height:44px}
.feature-card p{margin-left:28px;font-size:14.5px;line-height:26px}

/* problem */
.problem-title{position:absolute;left:111px;top:890px;font-weight:800;font-size:29px;line-height:35px;color:var(--ink);text-transform:uppercase}
.kicker{font-family:"Montserrat",sans-serif;font-weight:700;font-size:14px;color:var(--green);text-transform:uppercase;line-height:26px}
.screen{position:absolute;border-radius:10px}

/* why */
.why{position:absolute;top:1262px;left:0;width:1200px;height:660px;background:linear-gradient(120deg,#1b7fcf 0%,#3aa0e0 50%,#2b8ad6 100%)}
.why h2{position:absolute;top:155px;width:1200px;text-align:center;color:var(--white);font-weight:700;font-size:30px;text-transform:uppercase}
.why-col{position:absolute;top:328px;color:var(--white);text-align:center}
.why-col h3{font-weight:700;font-size:18px;line-height:26px;text-transform:uppercase}
.why-col .rule{width:28px;height:2px;background:var(--white);margin:14px auto 18px}
.why-col p{font-size:14.5px;line-height:28.5px}
.why-ic{position:absolute;top:-70px;left:50%;margin-left:-24px;width:48px;height:48px}
.chev-list{list-style:none;font-size:14.5px;line-height:25.5px;text-align:left}
.chev-list li::before{content:"»";margin-right:16px;font-weight:700}

/* scary */
.scary-title{position:absolute;left:588px;top:2090px;font-weight:800;font-size:29px;line-height:35px;color:var(--ink);text-transform:uppercase}
.stats{position:absolute;left:588px;top:2284px;display:flex;align-items:baseline;gap:16px;font-family:"Montserrat",sans-serif;font-weight:700;color:var(--blue)}
.stats .big{font-size:22px}
.stats .small{font-size:14px;color:var(--ink)}

/* plan */
.plan{position:absolute;top:2495px;left:0;width:1200px;height:675px;background:linear-gradient(180deg,#ffffff 0%,#eef0f1 60%,#e9ebec 100%)}
.plan h2{position:absolute;top:92px;width:1200px;text-align:center;font-weight:700;font-size:30px;color:var(--ink);text-transform:uppercase}
.step{position:absolute;top:300px;text-align:center}
.step .num{font-family:"Montserrat",sans-serif;font-weight:700;font-size:26px;color:var(--green)}
.step h3{font-size:14px;font-weight:700;color:var(--ink);line-height:25px;margin-top:8px;text-transform:uppercase}
.step p{font-size:14.5px;line-height:25px;color:var(--muted);margin-top:14px}
.step .chev-list{color:var(--muted);line-height:29px;margin-top:12px;display:inline-block}
.step .chev-list li::before{color:var(--blue)}
.divider{position:absolute;top:300px;width:1px;height:210px;background:#d9dbdc}

/* cta band */
.band{position:absolute;top:3170px;left:0;width:1200px;height:260px;background:var(--green-band)}
.band h2{position:absolute;left:111px;top:132px;color:var(--white);font-weight:800;font-size:29px;line-height:35px;text-transform:uppercase}
.band .ring{position:absolute;left:111px;top:45px;width:56px;height:56px;border-radius:50%;border:2px solid var(--white);display:flex;align-items:center;justify-content:center}

/* footer */
.footer-col{position:absolute;top:3487px}
.footer-col h4{font-family:"Montserrat",sans-serif;font-weight:800;font-size:24px;color:var(--ink);line-height:34px}
.footer-col ul{list-style:none;margin-top:14px;font-size:14.5px;line-height:34.5px;color:var(--muted)}
.footer-col li::before{content:"»";color:var(--blue);margin-right:14px;font-weight:700}
.footer-about{font-size:14.5px;line-height:30px;color:var(--muted);margin-top:14px;width:270px}
.bottom-bar{position:absolute;top:3836px;left:0;width:1200px;height:47px;background:var(--blue);color:var(--white);font-size:14px;display:flex;align-items:center;justify-content:center}
.bottom-bar .code{position:absolute;right:37px;font-size:12px}
</style>
</head>
<body>

<svg width="0" height="0" style="position:absolute">
  <defs>
    <symbol id="arrow-circle" viewBox="0 0 16 16"><circle cx="8" cy="8" r="8" fill="#fff"/><path d="M6.5 4.5 10 8l-3.5 3.5" stroke="#2f8fd8" stroke-width="2" fill="none"/></symbol>
    <symbol id="arrow-circle-g" viewBox="0 0 16 16"><circle cx="8" cy="8" r="8" fill="#fff"/><path d="M6.5 4.5 10 8l-3.5 3.5" stroke="#7ab648" stroke-width="2" fill="none"/></symbol>
    <symbol id="people" viewBox="0 0 30 30" fill="none" stroke="#fff" stroke-width="1.6"><circle cx="15" cy="9" r="3.5"/><circle cx="8" cy="12" r="2.6"/><circle cx="22" cy="12" r="2.6"/><path d="M9 24c0-4 3-7 6-7s6 3 6 7M3 24c0-3 2-6 5-6M27 24c0-3-2-6-5-6"/></symbol>
  </defs>
</svg>

<header class="site-header">
  <div class="brand" style="left:112px;top:20px"><span class="brand-dot"></span><span class="brand-name">CrewBeacon</span></div>
  <nav class="nav"><span class="active">HOME</span><span>BUY ADDONS</span><span>CUST LOGIN</span></nav>
  <a class="btn" style="left:864px;top:18px;width:224px">Explore your choices <svg><use href="#arrow-circle"/></svg></a>
</header>

<section class="hero" role="img" aria-label="Office desk with a desk phone, softly blurred background">
  <h1 class="hero-title">Feel confident that your<br>staff is protected</h1>
  <p class="hero-sub">Get a revolutionary new electronic panic button</p>
  <a class="btn" style="left:487px;top:350px;width:224px">Ready to get started <svg><use href="#arrow-circle"/></svg></a>
</section>

<div class="feature-card" style="left:112px;width:319px;background:var(--blue)">
  <div class="ic"><svg viewBox="0 0 44 44" fill="none" stroke="#fff" stroke-width="1.6"><rect x="5" y="8" width="34" height="30" rx="2"/><path d="M5 15h34M13 5v6M31 5v6"/><circle cx="22" cy="27" r="7"/><path d="M22 23v4l3 2"/></svg></div>
  <p>Problems Stopped Before<br>They Start For Any Type Of<br>Organization</p>
</div>
<div class="feature-card" style="left:442px;width:318px;background:var(--green)">
  <div class="ic"><svg viewBox="0 0 44 44" fill="none" stroke="#fff" stroke-width="1.6"><circle cx="24" cy="15" r="10"/><path d="M20 19l8-8"/><circle cx="20.5" cy="11.5" r="1.3"/><circle cx="27.5" cy="18.5" r="1.3"/><path d="M3 33h7l8 3h10l10-6"/><path d="M10 30h10"/></svg></div>
  <p>Affordable Prices Starting at<br>$18 per month. No Contracts.<br>No Hidden Costs.</p>
</div>
<div class="feature-card" style="left:770px;width:318px;background:var(--blue)">
  <div class="ic"><svg viewBox="0 0 44 44" fill="none" stroke="#fff" stroke-width="1.6"><path d="M15 26a10 10 0 1 1 14 0c-2 2-2 4-2 6H17c0-2 0-4-2-6z"/><path d="M17 36h10M18 40h8M4 17h4M36 17h4M8 6l3 3M36 6l-3 3"/></svg></div>
  <p>Alerts by computer, mobile<br>device, text, phone, email,<br>monitoring and E911</p>
</div>

<!-- problem -->
<div class="icon-badge" style="left:111px;top:818px"><svg><use href="#people"/></svg></div>
<h2 class="problem-title">Your empoyees shouldn’t<br>feel alone when they<br>need help</h2>
<p class="kicker abs" style="left:111px;top:1017px">Does this problem make you feel frustrated and anxious?</p>
<p class="abs" style="left:111px;top:1062px;font-size:15px">Put a simple solution in their hands</p>
<a class="btn" style="left:112px;top:1110px;width:224px">Ready to get started <svg><use href="#arrow-circle"/></svg></a>
<div class="screen" style="left:722px;top:851px;width:392px;height:252px;background:#1c1c1e"></div>
<div class="screen" role="img" aria-label="Explainer video still: worried character next to a panic button, with play control" style="left:732px;top:861px;width:372px;height:232px;border-radius:2px;background:linear-gradient(180deg,#f4f4f4 0%,#e4e4e4 70%,#8a8a8a 72%,#7d7d7d 100%)"></div>
<div class="screen" style="left:641px;top:1103px;width:550px;height:18px;border-radius:0 0 14px 14px;background:linear-gradient(180deg,#c9cbcd,#8e9093)"></div>

<!-- why -->
<section class="why">
  <div class="icon-badge" style="left:572px;top:77px"><svg viewBox="0 0 30 30" fill="none" stroke="#fff" stroke-width="1.6"><circle cx="15" cy="10" r="6"/><path d="M15 7v6M13 9h3.5M3 23h6l6 2h7l6-4"/></svg></div>
  <h2>Why businesses choose us</h2>

  <div class="why-col" style="left:135px;width:250px">
    <svg class="why-ic" viewBox="0 0 48 48" fill="none" stroke="#fff" stroke-width="1.6"><rect x="8" y="26" width="14" height="12"/><rect x="24" y="22" width="16" height="16"/><path d="M22 6h14v12H22zM4 42h40"/><path d="M29 10h2M12 30h6M28 28h8"/></svg>
    <h3>Easy to use</h3><div class="rule"></div>
    <p>Press a button and let the right<br>people know you need help and open a<br>chat window letting everyone talk on<br>resolving their problem.</p>
  </div>

  <div class="why-col" style="left:475px;width:250px">
    <svg class="why-ic" viewBox="0 0 48 48" fill="none" stroke="#fff" stroke-width="1.6"><rect x="6" y="8" width="36" height="26" rx="1"/><path d="M18 42h12M24 34v8"/><rect x="14" y="14" width="12" height="9"/><rect x="22" y="19" width="12" height="9"/></svg>
    <h3>Communicate the<br>way you want</h3>
    <div style="display:flex;gap:40px;justify-content:center;margin-top:22px">
      <ul class="chev-list"><li>Computer</li><li>Mobile</li><li>Email</li><li>Phone call</li></ul>
      <ul class="chev-list"><li>Text</li><li>E911</li><li>Call Center</li></ul>
    </div>
  </div>

  <div class="why-col" style="left:790px;width:310px">
    <svg class="why-ic" viewBox="0 0 48 48" fill="none" stroke="#fff" stroke-width="1.6"><path d="M24 4l16 6v12c0 11-7 18-16 22C15 40 8 33 8 22V10z"/><circle cx="24" cy="23" r="8"/><path d="M20 23l3 3 5-6"/></svg>
    <h3>Cost effective protection</h3><div class="rule"></div>
    <p>By leveraging your existing<br>network and equipment we can lower<br>your costs to give better options to<br>your staff.</p>
  </div>

  <a class="btn green" style="left:488px;top:561px;width:224px">Ready to get started <svg><use href="#arrow-circle-g"/></svg></a>
</section>

<!-- scary -->
<div class="screen" style="left:72px;top:2060px;width:390px;height:256px;background:#1c1c1e"></div>
<div class="screen" role="img" aria-label="Illustration panels showing workplace threats: criminal, severe weather, robbery, disgruntled employee, active shooter, domestic dispute" style="left:82px;top:2072px;width:370px;height:234px;border-radius:2px;background:linear-gradient(90deg,#f6f6f6 0%,#ececec 50%,#f3f3f3 100%)"></div>
<div class="screen" style="left:8px;top:2316px;width:535px;height:18px;border-radius:0 0 14px 14px;background:linear-gradient(180deg,#c9cbcd,#8e9093)"></div>

<div class="icon-badge" style="left:588px;top:2018px"><svg><use href="#people"/></svg></div>
<h2 class="scary-title">We know how scary it can<br>feel to worry about employee<br>safety.</h2>
<p class="kicker abs" style="left:588px;top:2218px;font-size:13.5px">That’s why we have provided a way for&nbsp; customers to get<br>help to staff effectively in</p>
<div class="stats"><span class="big">45 STATES</span><span class="small">COVERING</span><span class="big">5 COUNTRIES</span></div>
<a class="btn" style="left:589px;top:2329px;width:224px">Ready to get started <svg><use href="#arrow-circle"/></svg></a>

<!-- plan -->
<section class="plan">
  <div class="icon-badge" style="left:572px;top:39px"><svg viewBox="0 0 30 30" fill="none" stroke="#fff" stroke-width="1.6"><rect x="7" y="4" width="16" height="22" rx="1"/><path d="M11 10h8M11 14h8M11 18h5"/></svg></div>
  <h2>Simple start plan</h2>
  <svg class="abs" style="left:0;top:140px" width="1200" height="150" viewBox="0 0 1200 150" fill="none" stroke="#2f8fd8" stroke-width="2">
    <path d="M600 5c-40 40-200 20-330 30-60 5-90 40-32 90"/>
    <path d="M600 5c40 40 200 20 330 30 60 5 90 40 32 90"/>
    <path d="M600 5c-20 40-5 60 20 90 15 20 15 40 13 55"/>
    <path d="M232 120l6 9 5-10M956 120l6 9 5-10M627 140l6 9 5-10" fill="#2f8fd8"/>
  </svg>
  <div class="step" style="left:110px;width:230px"><div class="num">01</div><h3>Explore your choices</h3><ul class="chev-list"><li>Pricing</li><li>Trial</li><li>Quote</li><li>Hardware</li></ul></div>
  <div class="divider" style="left:424px"></div>
  <div class="step" style="left:508px;width:240px"><div class="num">02</div><h3>Get setup</h3><ul class="chev-list"><li>Input Your Alerts</li><li>Input Your Staff</li><li>Install Our Software</li></ul></div>
  <div class="divider" style="left:789px"></div>
  <div class="step" style="left:845px;width:270px"><div class="num">03</div><h3>Feel confident your staff<br>is protected</h3><p>High Five. You just too a major step<br>to getting&nbsp; rid of the anxiety and<br>frustration this gave&nbsp; you.</p></div>
  <a class="btn" style="left:514px;top:545px;width:172px">Start my demo <svg><use href="#arrow-circle"/></svg></a>
</section>

<!-- band -->
<section class="band">
  <div class="ring"><svg width="30" height="30"><use href="#people"/></svg></div>
  <h2>Stay connected with staff<br>during a crisis situations</h2>
  <a class="btn" style="left:856px;top:106px;width:174px">Start my demo <svg><use href="#arrow-circle"/></svg></a>
</section>

<!-- footer -->
<div class="footer-col" style="left:109px">
  <h4>CALL US<br>1-800-555-0142</h4>
  <p class="footer-about">When employees feel alone during a threatening situation, we give them a way to let the right resources know that they need help so you can feel&nbsp; confident that your staff is protected.</p>
  <div class="brand" style="position:relative;margin-top:26px"><span class="brand-dot" style="width:62px;height:62px"></span><span class="brand-name" style="font-size:38px">CrewBeacon</span></div>
</div>
<div class="footer-col" style="left:485px"><h4>SHOP</h4><ul><li>Add Ons</li><li>Start My Demo</li><li>Custom Quote</li><li>Start Trial</li></ul></div>
<div class="footer-col" style="left:718px"><h4>ABOUT</h4><ul><li>Affiliates</li><li>Contact</li><li>Support</li><li>Existing Customers</li><li>Industries</li><li>Blog</li><li>FAQ</li></ul></div>
<div class="footer-col" style="left:948px"><h4>LEGAL</h4><ul><li>Privacy Policy</li><li>Terms of Use</li><li>End User License</li><li>Agreement</li></ul></div>

<footer class="bottom-bar">© 2020 CrewBeacon. All Rights Reserved <span class="code">C42</span></footer>

</body>
</html>
```